Online Psychology Practice needs business cards.

Online Psychology service needs business cards. Have own logo- please see uploaded. I have other file formats if you need (not sure one needed?)

Details for Business Card:
Fiona Kettlewood
Clinical Psychologist BPsych, BPsych (Hons), MPsych (Clin), MAPS
T: 0457260714 | F: 08 71526804
E: hello@harbourlightmindcarestudio.com.au
W: harbourlightmindcarestudio.com.au

Industry/Entity Type

Health

Contact Information for Business Card

Logo plus details above (couldn't write in this section)

```html
<!DOCTYPE html>
<html lang="en">
<head>
<meta charset="utf-8">
<title>Harbourlight Mindcare Studio – Business Cards</title>
<link href="https://fonts.googleapis.com/css2?family=Poppins:wght@400;600&display=swap" rel="stylesheet">
<style>
  :root {
    --navy: #1a5a85;
    --teal: #1b93a8;
    --card: #ffffff;
    --ghost: #eef0f4;
    --backdrop: #2b2b2d;
  }
  * { margin: 0; padding: 0; box-sizing: border-box; }
  html, body {
    width: 1200px; height: 900px; overflow: hidden;
    background: var(--backdrop);
    font-family: "Poppins", sans-serif;
  }
  .stage { position: relative; width: 1200px; height: 900px; }
  .card {
    position: absolute; width: 640px; height: 366px;
    background: var(--card); border-radius: 26px; overflow: hidden;
    box-shadow: 0 14px 30px rgba(0,0,0,.45);
  }
  .card--front { left: 80px; top: 60px; }
  .card--back { left: 480px; top: 474px; }

  .ghost-disc {
    position: absolute; right: -70px; top: -90px;
    width: 340px; height: 340px; border-radius: 50%;
    background: var(--ghost);
  }
  .brand {
    position: absolute; display: flex; align-items: center; gap: 14px;
    color: var(--navy); font-weight: 600;
  }
  .brand__dot { flex: none; border-radius: 50%; background: var(--navy); }
  .card--front .brand { left: 168px; top: 128px; font-size: 30px; line-height: 1.1; }
  .card--front .brand__dot { width: 70px; height: 70px; }
  .card--back .brand { right: 34px; top: 44px; font-size: 22px; line-height: 1.1; }
  .card--back .brand__dot { width: 52px; height: 52px; }

  .person { position: absolute; left: 34px; top: 48px; }
  .person__name { color: var(--navy); font-weight: 600; font-size: 27px; line-height: 1.1; }
  .person__role { color: var(--teal); font-size: 14.5px; line-height: 1.35; margin-top: 6px; }

  .swoosh { position: absolute; left: 0; top: 0; }

  .contacts {
    position: absolute; left: 40px; top: 256px; list-style: none;
    color: var(--navy); font-size: 16.5px; line-height: 24px;
  }
  .contacts li { display: flex; align-items: center; gap: 10px; }
  .contacts svg { width: 15px; height: 15px; flex: none; fill: var(--teal); }
  .contacts .icon-line { fill: none; stroke: var(--teal); stroke-width: 1.4; }
</style>
</head>
<body>
<main class="stage">

  <section class="card card--front">
    <div class="ghost-disc"></div>
    <div class="brand">
      <span class="brand__dot"></span>
      <span>Harbourlight<br>Mindcare Studio</span>
    </div>
  </section>

  <section class="card card--back">
    <svg class="swoosh" width="640" height="366" viewBox="0 0 640 366" aria-hidden="true">
      <defs>
        <linearGradient id="swooshTone" x1="0" x2="1">
          <stop offset="0" stop-color="#1a5a85"/>
          <stop offset="1" stop-color="#1b93a8"/>
        </linearGradient>
      </defs>
      <path d="M0,240 C120,192 260,182 380,182 C480,180 570,156 622,118 C578,166 482,192 380,192 C260,192 130,204 0,246 Z" fill="url(#swooshTone)"/>
    </svg>

    <div class="person">
      <h1 class="person__name">Fiona Kettlewood</h1>
      <p class="person__role">Clinical Psychologist BPsych,<br>BPsych (Hons), MPsych (Clin), MAPS</p>
    </div>

    <div class="brand">
      <span class="brand__dot"></span>
      <span>Harbourlight<br>Mindcare Studio</span>
    </div>

    <ul class="contacts">
      <li><svg viewBox="0 0 16 16"><path d="M3 1h3l1.5 4-2 1.2a9 9 0 0 0 4.3 4.3L11 8.5l4 1.5v3a2 2 0 0 1-2 2A13 13 0 0 1 1 3a2 2 0 0 1 2-2z"/></svg>0457260714</li>
      <li><svg viewBox="0 0 16 16"><path d="M4 1h8v4H4zM1 6h14v6h-3v3H4v-3H1zM5 10v4h6v-4z"/></svg>08 71526804</li>
      <li><svg viewBox="0 0 16 16"><path d="M1 3h14v10H1zM2.5 4.5 8 9l5.5-4.5v-.2h-11z"/></svg>hello@harbourlightmindcarestudio.com.au</li>
      <li><svg viewBox="0 0 16 16"><g class="icon-line"><circle cx="8" cy="8" r="6.3"/><ellipse cx="8" cy="8" rx="2.7" ry="6.3"/><path d="M1.7 8h12.6M2.8 4.8h10.4M2.8 11.2h10.4"/></g></svg>harbourlightmindcarestudio.com.au</li>
    </ul>
  </section>

</main>
</body>
</html>
```